Silent Auction Design Piece (11x14, Full Color)

I am needing to build a new Silent auction piece. This one will be for Sport Courts. (Pickleball, Tennis, and Basketball) I will attach pics and a narrative). I would like to maintain the Black and Gold Theme but possibly change the lettering and motif to show more youth, fun and excitement around sports. Also remove pictures of my face and credentials. Use credentials but say it is from our professional team of designers.
Target Market(s)
Fundraising Gala Events (High Net Worth Customers)
Industry/Entity Type
Design & Architecture
Requirements
Must have
- Black and Gold Colors, Images oof Sport Courts, Narrative (see attached, Choose 1 of 5))
Nice to have
- Easy to read, make this piece exciting & attractive. We are selling to high end consumers!
Should not have
- Poor lettering, only bespoke fonts.

```html
<!DOCTYPE html>
<html lang="en">
<head>
<meta charset="UTF-8">
<title>Silent Auction – Sport Court Design Experience</title>
<link href="https://fonts.googleapis.com/css2?family=Inter:wght@400;500;600;700&display=swap" rel="stylesheet">
<style>
  :root {
    --ink: #050505;
    --gold: #d8be86;
    --gold-light: #ecdcae;
    --cream: #efe7d2;
    --rule: #c9ad6e;
    --court-green: #3f8a3a;
    --court-blue: #2f3f86;
    --villa-white: #dfe3e4;
  }
  * { margin: 0; padding: 0; box-sizing: border-box; }
  html, body { width: 947px; height: 1200px; overflow: hidden; background: var(--ink); }
  body { font-family: "Inter", sans-serif; color: var(--cream); position: relative; }

  .eyebrow {
    position: absolute; top: 38px; left: 0; width: 947px; text-align: center;
    font-size: 29px; font-weight: 400; color: var(--cream); letter-spacing: 0.2px;
  }
  .headline {
    position: absolute; top: 88px; left: 0; width: 947px; text-align: center;
    font-size: 61px; font-weight: 500; color: var(--gold-light); letter-spacing: -0.5px;
  }
  .hero-photo {
    position: absolute; top: 183px; left: 60px; width: 828px; height: 309px;
    background: linear-gradient(100deg, #2f5a2b 0%, var(--court-green) 22%, var(--court-blue) 34%, #5d7a4c 46%, var(--villa-white) 62%, #c9d0d2 78%, #3c5f73 100%);
  }
  .offer-title {
    position: absolute; top: 520px; left: 0; width: 947px; text-align: center;
    font-size: 42px; font-weight: 600; line-height: 50px; color: var(--gold); letter-spacing: 0.3px;
  }
  .tagline {
    position: absolute; top: 634px; left: 0; width: 947px; text-align: center;
    font-size: 19px; font-weight: 400; color: var(--cream);
  }
  .rule { position: absolute; left: 54px; width: 834px; height: 2px; background: var(--rule); }
  .rule--top { top: 690px; }
  .rule--bottom { top: 1015px; }

  .narrative {
    position: absolute; top: 708px; left: 60px; width: 412px;
    font-size: 12.4px; line-height: 14.6px; color: var(--cream);
  }
  .narrative p { margin-bottom: 6px; }
  .column-divider { position: absolute; top: 713px; left: 477px; width: 2px; height: 283px; background: var(--rule); }

  .bid-table { position: absolute; top: 713px; left: 497px; width: 375px; height: 130px; }
  .bid-cell {
    position: absolute; width: 170px; text-align: center;
    font-size: 13px; font-weight: 600; line-height: 17px; color: var(--cream); letter-spacing: 0.2px;
  }
  .bid-cell .value { font-size: 14px; font-weight: 600; }
  .cell-a { left: 0; top: 6px; }
  .cell-b { left: 204px; top: 6px; }
  .cell-c { left: 0; top: 72px; }
  .cell-d { left: 204px; top: 72px; }
  .bid-table svg { position: absolute; left: 0; top: 0; }

  .call-to-action {
    position: absolute; top: 866px; left: 497px; width: 375px; text-align: center;
    font-size: 19px; font-weight: 500; line-height: 24px; color: var(--gold-light);
  }

  .donor { position: absolute; top: 1060px; left: 0; width: 947px; text-align: center; }
  .donor-line { font-size: 19px; font-weight: 500; color: var(--gold-light); }
  .donor-name { text-decoration: underline; text-underline-offset: 3px; }
  .contact-line { margin-top: 8px; font-size: 19px; color: var(--cream); }
  .terms-line { margin-top: 10px; font-size: 17px; color: var(--cream); }
</style>
</head>
<body>
  <div class="eyebrow">Non-Profit Piece for Sport Courts</div>
  <h1 class="headline">Tech-Focused Innovation</h1>

  <div class="hero-photo" role="img" aria-label="Aerial photo of a luxury modern villa with a blue tennis court on green surround, lounge terrace and infinity pool"></div>

  <h2 class="offer-title">EXCLUSIVE TECH-ADVANCED SPORT<br>COURT DESIGN EXPERIENCE</h2>
  <div class="tagline">Revolutionize Your Outdoor Space with State-of-the-Art Innovation</div>

  <div class="rule rule--top"></div>

  <div class="narrative">
    <p>Elevate your home with a custom sport court powered by the professional design team at Solano Courts. As a dedicated supporter of [Non-Profit Organization/Gala], proudly offers this package:</p>
    <p>Expert Consultation &amp; Innovative Design: Collaborate with our specialists to design a high-tech multi-court (pickleball, basketball, tennis, and multi-sport) featuring smart LED systems, and app-controlled integration, paired with elegant landscaping.</p>
    <p>Premium Inclusions: On-site evaluation, visualization, 3D visualizations, and tech specs, blueprint redeemable toward installation.</p>
    <p>Tailored to You: Adaptable to any luxury residence, blending athletic and aesthetic appeal. Valued at $2,500, this package showcases Solano's commitment to future-forward court solutions.</p>
    <p>Redeem within 12 months.</p>
  </div>

  <div class="column-divider"></div>

  <div class="bid-table">
    <svg width="375" height="130" aria-hidden="true">
      <line x1="183" y1="2" x2="183" y2="107" stroke="#c9ad6e" stroke-width="2"/>
      <line x1="0" y1="41" x2="168" y2="41" stroke="#c9ad6e" stroke-width="2"/>
      <line x1="212" y1="41" x2="375" y2="41" stroke="#c9ad6e" stroke-width="2"/>
      <line x1="0" y1="60" x2="168" y2="60" stroke="#c9ad6e" stroke-width="2"/>
      <line x1="208" y1="60" x2="375" y2="60" stroke="#c9ad6e" stroke-width="2"/>
      <line x1="0" y1="128" x2="375" y2="128" stroke="#c9ad6e" stroke-width="2"/>
    </svg>
    <div class="bid-cell cell-a">RETAIL VALUE:<br><span class="value">$500</span></div>
    <div class="bid-cell cell-b">RETAIL VALUE:<br><span class="value">$199</span></div>
    <div class="bid-cell cell-c">MINIMUM BID<br><span class="value">$199</span></div>
    <div class="bid-cell cell-d">BID INCREMENTS<br><span class="value">50</span></div>
  </div>

  <div class="call-to-action">Bid Today to Unlock the<br>Future of Home Sports!</div>

  <div class="rule rule--bottom"></div>

  <div class="donor">
    <div class="donor-line">DONATED BY: <span class="donor-name">Solano Courts</span></div>
    <div class="contact-line">info@solanocourts.com | www.solanocourts.com</div>
    <div class="terms-line">Non-transferable. No cash value. Subject to availability and terms.</div>
  </div>
</body>
</html>
```